Stationery For Upscale Concierge Company

Create stationary that looks good in black and white and uses the attached logo. Needs to be upscale using upscale fonts and layout. Use the attached logo. Reverse out if necessary.

```html
<!DOCTYPE html>
<html lang="en">
<head>
<meta charset="utf-8">
<title>Astor Lane Stationery</title>
<link href="https://fonts.googleapis.com/css2?family=Cinzel:wght@400&family=Roboto:wght@400;500&family=Great+Vibes&display=swap" rel="stylesheet">
<style>
:root{
  --backdrop:#d0d0d0;
  --paper:#f1f1f1;
  --ink:#3a3a3b;
  --text:#444446;
  --white:#ffffff;
  --signature:#3f5a86;
}
*{margin:0;padding:0;box-sizing:border-box}
html,body{width:1200px;height:848px;overflow:hidden;background:var(--backdrop)}
.canvas{position:relative;width:1200px;height:848px}
.sheet{position:absolute;background:var(--paper);overflow:hidden}
.brand{font-family:"Cinzel",serif;font-weight:400;color:var(--ink);letter-spacing:.06em;white-space:nowrap}
.body{font-family:"Roboto",sans-serif;color:var(--text)}
.footer-band{position:absolute;left:0;bottom:0;width:100%;background:var(--ink)}
.footer-band::before{content:"";position:absolute;left:0;right:0;top:-5px;height:2px;background:var(--ink)}
.contact{position:absolute;font-family:"Roboto",sans-serif;color:var(--white);text-align:right;line-height:1.55}
.contact .row{display:flex;justify-content:flex-end;align-items:center;gap:6px;white-space:nowrap}
.contact svg{width:6px;height:6px;flex:none}

/* letterhead */
.letterhead{left:114px;top:146px;width:422px;height:595px}
.letterhead .brand{position:absolute;left:27px;top:48px;font-size:11px}
.letter{position:absolute;left:26px;top:130px;width:372px;font-size:6.6px;line-height:1.45}
.letter .date{margin-bottom:22px}
.letter .recipient{margin-bottom:22px}
.letter strong{font-weight:500}
.letter p{text-align:justify;margin-bottom:10px}
.letter .salutation{margin-bottom:10px}
.signoff{margin-top:32px}
.signature{font-family:"Great Vibes",cursive;color:var(--signature);font-size:14px;margin:3px 0 4px 0}
.letterhead .footer-band{height:72px}
.letterhead .contact{right:18px;bottom:14px;font-size:6px}

/* business cards */
.card{top:105px;width:182px;height:110px}
.card-front{left:630px;background:var(--ink);display:flex;align-items:center;justify-content:center}
.card-front .brand{color:var(--white);font-size:11px}
.card-back{left:848px}
.card-back .brand{position:absolute;left:10px;top:40px;font-size:8.5px}
.card-back .person{position:absolute;right:9px;top:16px;text-align:right}
.card-back .person .name{font-family:"Cinzel",serif;font-size:7px;color:var(--ink)}
.card-back .person .role{font-family:"Roboto",sans-serif;font-size:3.6px;color:var(--text)}
.card-back .address{position:absolute;left:10px;top:64px;font-size:4.2px;line-height:1.5}
.card-back .footer-band{height:28px}
.card-back .contact{right:7px;bottom:5px;font-size:4.2px}
.card-back .contact svg{width:4px;height:4px}

/* envelope front */
.envelope-front{left:574px;top:239px;width:510px;height:230px}
.envelope-front .brand{position:absolute;left:30px;top:62px;font-size:12px}
.envelope-front .footer-band{height:72px}
.envelope-front .contact{right:18px;bottom:14px;font-size:5.8px}

/* envelope back */
.envelope-back{left:576px;top:502px;width:510px;height:230px}
.flap{position:absolute;left:0;top:0;width:510px;height:64px}
.envelope-back .brand{position:absolute;left:0;right:0;top:24px;text-align:center;color:var(--white);font-size:9px}
.envelope-back .web{position:absolute;left:0;right:0;bottom:21px;text-align:center;font-family:"Roboto",sans-serif;font-size:6px;letter-spacing:.4em;color:var(--text)}
</style>
</head>
<body>
<main class="canvas">

  <section class="sheet letterhead" aria-label="Letterhead">
    <div class="brand">ASTOR LANE</div>
    <div class="letter body">
      <div class="date">30/20/2016</div>
      <div class="recipient"><strong>Mr. Alan Brooks</strong><br>45 Elm Avenue, Unit 12,<br>Northbridge<br>Postcode-2063</div>
      <div class="salutation">Dear Sir,</div>
      <p>Lorem Ipsum is simply dummy text of the printing and typesetting industry. Lorem Ipsum has been the industry's standard dummy text ever since the 1500s, when an unknown printer took a galley of type and scrambled it to make a type specimen book. It has survived not only five centuries, but also the leap into electronic typesetting, remaining essentially unchanged. It was popularised in the 1960s with the release of transfer sheets containing Lorem Ipsum passages, and more recently with desktop publishing software and modern layout tools including versions of Lorem Ipsum.</p>
      <p>Lorem Ipsum is simply dummy text of the printing and typesetting industry. Lorem Ipsum has been the industry's standard dummy text ever since the 1500s, when an unknown printer took a galley of type and scrambled it to make a type specimen book. It has survived not only five centuries, but also the leap into electronic typesetting, remaining essentially unchanged. It was popularised in the 1960s with the release of transfer sheets containing Lorem Ipsum passages, and more recently with desktop publishing software and modern layout tools including versions of Lorem Ipsum.</p>
      <p>Lorem Ipsum is simply dummy text of the printing and typesetting industry. Lorem Ipsum has been the industry's standard dummy text ever since the 1500s, when an unknown printer took a galley of type and scrambled it to make a type specimen book.</p>
      <p>Lorem Ipsum is simply dummy text of the printing and typesetting industry. Lorem Ipsum has been the industry's standard dummy text ever since the 1500s, when an unknown printer took a galley of type and scrambled it to make a type specimen book.</p>
      <div class="signoff"><strong>Your Name</strong></div>
      <div class="signature">Your Signature</div>
      <div>CEO &nbsp;|&nbsp; Owner</div>
    </div>
    <div class="footer-band" aria-hidden="true"></div>
    <div class="contact">
      <div class="row">0100-555-210 <svg viewBox="0 0 6 6"><rect x="1" y="1" width="4" height="4" rx="1" fill="#fff"/></svg></div>
      <div class="row">www.astorlane.com <svg viewBox="0 0 6 6"><rect x=".5" y="1.2" width="5" height="3.6" fill="#fff"/></svg></div>
      <div class="row">peter.hale@astorlane.com <svg viewBox="0 0 6 6"><circle cx="3" cy="3" r="2.5" fill="#fff"/></svg></div>
      <div class="row" style="margin-top:3px">78 Harbour Row, Sydney NSW 2000, Postcode</div>
    </div>
  </section>

  <section class="sheet card card-front" aria-label="Business card front">
    <div class="brand">ASTOR LANE</div>
  </section>

  <section class="sheet card card-back" aria-label="Business card back">
    <div class="brand">ASTOR LANE</div>
    <div class="person"><div class="name">PETER HALE</div><div class="role">Managing Director</div></div>
    <div class="address body">78 Harbour Row, Sydney<br>NSW 2000, Postcode</div>
    <div class="footer-band" aria-hidden="true"></div>
    <div class="contact">
      <div class="row">0100-555-210 <svg viewBox="0 0 6 6"><rect x="1" y="1" width="4" height="4" rx="1" fill="#fff"/></svg></div>
      <div class="row">www.astorlane.com <svg viewBox="0 0 6 6"><rect x=".5" y="1.2" width="5" height="3.6" fill="#fff"/></svg></div>
      <div class="row">peter.hale@astorlane.com <svg viewBox="0 0 6 6"><circle cx="3" cy="3" r="2.5" fill="#fff"/></svg></div>
    </div>
  </section>

  <section class="sheet envelope-front" aria-label="Envelope front">
    <div class="brand">ASTOR LANE</div>
    <div class="footer-band" aria-hidden="true"></div>
    <div class="contact">
      <div class="row">0100-555-210 <svg viewBox="0 0 6 6"><rect x="1" y="1" width="4" height="4" rx="1" fill="#fff"/></svg></div>
      <div class="row">www.astorlane.com <svg viewBox="0 0 6 6"><rect x=".5" y="1.2" width="5" height="3.6" fill="#fff"/></svg></div>
      <div class="row">peter.hale@astorlane.com <svg viewBox="0 0 6 6"><circle cx="3" cy="3" r="2.5" fill="#fff"/></svg></div>
      <div class="row" style="margin-top:3px">78 Harbour Row, Sydney NSW 2000, Postcode</div>
    </div>
  </section>

  <section class="sheet envelope-back" aria-label="Envelope back">
    <svg class="flap" viewBox="0 0 510 64" aria-hidden="true">
      <path d="M0,0 H510 L474,46 Q462,62 440,62 H70 Q48,62 36,46 Z" fill="var(--ink)"/>
    </svg>
    <div class="brand">ASTOR LANE</div>
    <div class="web">www.astorlane.com</div>
  </section>

</main>
</body>
</html>
```